■ 依頼の目的/概要

私は第45回全国青葉学徒競技祭典選手権(以下、葉徒祭)運営委員会の広報局長を務めております。葉徒祭というのは、東日本と西日本から選抜された医学部学生が参加する体育大会で、開催競技は全12競技となっております。

今回は、その大会のPR用に各大学に配布するポスターのデザイン制作をお願いします。

■ 重視する点/検討基準

ポスターを見るのは主に大学医学部の学生で、一目見て葉徒祭のポスターだと分かるものがいいです。

制作する上で、必ず入れてほしいワードを以下に述べておきます。

・第45回全国青葉学徒競技祭典選手権
http://www.hatosai.kumonet.jp/top.htm(※大会HPです)
・主管:白鷺ヶ丘医療学院・浜風医療学院
・主催:北辰学徒競技協会連合・南星学徒競技協会連合
・開催競技(弓道・硬式テニス・軟式テニス・バトミントン・準硬式野球・サッカー・バスケットボール・柔道・卓球・剣道・バレーボール・ヨットの全12競技)

前年度、前々年度のポスターを添付しておりますので、ご参照下さい。

■ 利用用途

A2サイズのポスターに、片面カラーで印刷します。また、大会HPにも掲載いたします。

■ その他/注意点

データはイラストレーター形式(CS3以下)にて縦長使用でお願いします。
そのまま印刷会社に入稿するので、カラーモードはCMYKにて、塗り足し・アウトライン化もお願いします。

・ご提案を選択後に当選者様に修正を依頼する可能性がございますのでご了承下さい。
・選択させて頂いたデザインの著作権(財産権)等の扱いはMokkaro利用規約に従い、弊運営委員会に譲渡をお願いします。フォントや画像素材などを利用する場合は上記利用用途に使用できることを確認し、第三者の知的財産権等に注意して下さい。

葉徒祭につきましては下記のサイトをご参照下さい。何らかのご参考にしていただけると幸いです。また、第45回の大会HPはまだ制作しておりません。
http://www.hatosai.kumonet.jp/top.htm
http://ja.hyakkamori.jp/wiki/%E8%91%89%E5%BE%92%E7%A5%AD

以上、宜しくお願い致します。

たくさんのデザイン提案、どうもありがとうございます。
私1人だけでなく、実行委員何人かで最も相応しいと思われるものを選ばせて頂きたいと思います。
二週間位内には選びたいと思います。
■ 選んだ理由

医学生の部屋に貼っているイメージとの提案で、それが私たちのイメージにぴったりでした。また、大学に貼っていても目を引きそうなデザインでとても気に入りました。

■ 提案者全員のお礼・コメント

たくさんの提案ありがとうございました。
すばらしいものばかりだったので選ぶのに迷いましたが、委員何人かで話し合い今回はこのデザインを選ばせていただくことにしました。

```html
<!DOCTYPE html>
<html lang="ja">
<head>
<meta charset="utf-8">
<title>第45回 全国青葉学徒競技祭典選手権</title>
<link rel="stylesheet" href="https://fonts.googleapis.com/css2?family=Shippori+Mincho+B1:wght@800&family=Noto+Sans+JP:wght@700;900&display=swap">
<style>
  :root {
    --paper: #ffffff;
    --ink: #0d0b0b;
    --text: #ffffff;
    --accent: #d3121c;
  }
  * { margin: 0; padding: 0; box-sizing: border-box; }
  html, body { width: 855px; height: 1200px; overflow: hidden; background: var(--paper); }
  .poster {
    position: relative;
    width: 855px; height: 1200px;
    background: var(--paper);
  }
  .poster-field {
    position: absolute;
    inset: 12px;
    background: var(--ink);
  }
  .event-heading {
    position: absolute;
    left: 50px; top: 38px;
    font-family: "Shippori Mincho B1", serif;
    font-weight: 800;
    font-size: 54px;
    color: var(--text);
    letter-spacing: 1px;
    white-space: nowrap;
  }
  .event-heading .edition { font-size: 50px; margin-right: 14px; }
  .title-glyph {
    position: absolute;
    font-family: "Shippori Mincho B1", serif;
    font-weight: 800;
    font-size: 238px;
    line-height: 1;
    color: var(--accent);
  }
  .glyph-1 { left: 45px;  top: 160px; }
  .glyph-2 { left: 282px; top: 160px; }
  .glyph-3 { left: 520px; top: 160px; }
  .glyph-4 { left: 520px; top: 395px; }
  .glyph-5 { left: 520px; top: 630px; }
  .event-details {
    position: absolute;
    left: 50px; top: 900px;
    font-family: "Noto Sans JP", sans-serif;
    font-weight: 700;
    color: var(--text);
  }
  .sports-list { font-size: 21px; line-height: 31px; letter-spacing: 0.5px; white-space: nowrap; }
  .sports-total { margin-left: 10px; }
  .organizer { font-size: 21px; line-height: 31px; white-space: nowrap; }
  .organizer:first-of-type { margin-top: 12px; }
  .site-url {
    margin-top: 10px;
    font-family: "Noto Sans JP", sans-serif;
    font-weight: 900;
    font-size: 30px;
    letter-spacing: 0.5px;
    white-space: nowrap;
  }
</style>
</head>
<body>
  <main class="poster">
    <div class="poster-field"></div>

    <h1 class="event-heading"><span class="edition">第45回</span>全国青葉学徒競技</h1>

    <div class="title-mark" aria-label="祭典選手権">
      <span class="title-glyph glyph-1">祭</span>
      <span class="title-glyph glyph-2">典</span>
      <span class="title-glyph glyph-3">選</span>
      <span class="title-glyph glyph-4">手</span>
      <span class="title-glyph glyph-5">権</span>
    </div>

    <section class="event-details">
      <p class="sports-list">弓道・硬式テニス・軟式テニス・バトミントン・準硬式野球・サッカー<br>バスケットボール・柔道・卓球・剣道・バレーボール・ヨット<span class="sports-total">全12競技</span></p>
      <p class="organizer">主管：白鷺ヶ丘医療学院・浜風医療学院</p>
      <p class="organizer">主催：北辰学徒競技協会連合・南星学徒競技協会連合</p>
      <p class="site-url">http://www.hatosai.kumonet.jp/top.htm</p>
    </section>
  </main>
</body>
</html>
```